Milos Meadow Plant Hire WEB

Milos Meadow are a small family owned business specialising in hire of indoor horticultural plants. They have been operating for more than 20 years in the local New Zealand market providing long and short term plant hire for businesses and events.

They offer a wide range of mostly tropical and indigenous plants for hire and Milos Meadow staff maintain all hire plants on a regular basis.

MORE PHOTOS AVAILABLE ON REQUEST if required

Please note - this should be a small 3 pager - home/about - products - gallery
Contact Us can be a button or on home page. Note - this is a small owner operated business.

Target Market(s)

Commercial, offices, entrance foyers, receptions, restaurants, promotions, trade shows, events, corporate and private functions

Industry/Entity Type

Business

Requirements
Must have
• Must remain integral to existing branding and include the current company logo. Should maintain existing corporate colours. Requires an enquiry page for people to contact the company via email (this can be a mailto page), also requires a page explaining about the company, and one detailing the types of hire available together with types of plans for hire. The site also needs a gallery that can be added to over time to show the various plants and their applications.
Nice to have
• It would be nice to have a facility on the gallery where a couple of detail lines could be added to explain the plant types, location etc

PREFER A WORDPRESS SOLUTION - BUT OPEN TO SUGGESTIONS
Should not have
• The site should not be overly complex. It should be simple for the client to self manage (add/ remove photos, edit text) It should be quick to load and simple to navigate.

```html
<!DOCTYPE html>
<html lang="en">
<head>
<meta charset="utf-8">
<title>Milos Meadow – indoor plant hire</title>
<link rel="stylesheet" href="https://fonts.googleapis.com/css2?family=Questrial&family=Josefin+Sans:wght@400;600&display=swap">
<style>
:root{
  --header-top:#fafafa;
  --header-bottom:#e6e6e6;
  --ink:#2b2b2b;
  --text:#3a3a3a;
  --muted:#9a9a9a;
  --nav-top:#5d7590;
  --nav-bottom:#3d5168;
  --frame:#ffffff;
  --page:#e8e8e6;
  --panel:#f1f1ec;
  --box-line:#b9b9b5;
  --head-top:#5c6f84;
  --head-bottom:#2f3d4d;
  --field:#ececea;
  --field-line:#d6d6d2;
  --star:#f0b628;
  --footer:#242b35;
  --footer-bar:#3b4653;
  --footer-text:#ffffff;
  --footer-muted:#a7adb4;
}
*{box-sizing:border-box;margin:0;padding:0}
html,body{width:1029px;height:1200px;overflow:hidden}
body{position:relative;font-family:"Questrial",sans-serif;color:var(--text);background:var(--page)}
.abs{position:absolute}
h1,h2{font-weight:400}

/* header */
.site-header{left:0;top:0;width:1029px;height:110px;background:linear-gradient(var(--header-top),var(--header-bottom))}
.brand-name{left:124px;top:14px;font-family:"Josefin Sans",sans-serif;font-weight:600;font-size:36px;color:var(--ink);letter-spacing:1px}
.brand-tag{left:124px;top:76px;font-family:"Josefin Sans",sans-serif;font-weight:600;font-size:17px;letter-spacing:5.5px;color:var(--ink)}
.social{top:5px;width:28px;height:28px;border-radius:50%;background:#8a8f95;border:2px solid #c8cacc}
.header-phone{left:762px;top:54px;font-size:19px;color:var(--ink);display:flex;align-items:center;gap:2px}
.header-mail{left:758px;top:87px;font-size:11px;color:var(--ink);display:flex;align-items:center;gap:4px}

/* nav */
.main-nav{left:0;top:110px;width:1029px;height:31px;background:linear-gradient(var(--nav-top),var(--nav-bottom));border-top:1px solid #2c3a4a;border-bottom:1px solid #2c3a4a}
.main-nav a{position:absolute;top:9px;color:#fff;font-size:12px;text-decoration:none;text-transform:uppercase}

/* slider */
.slider-band{left:0;top:141px;width:1029px;height:393px;background:repeating-linear-gradient(45deg,#222 0 2px,#1a1a1a 2px 4px)}
.slider-frame{left:117px;top:141px;width:795px;height:393px;background:var(--frame)}
.slide-image{left:123px;top:148px;width:783px;height:379px;background:linear-gradient(90deg,#b9a892 0%,#cdbfab 30%,#8c8f87 50%,#6f9a52 72%,#d9d4c6 100%)}
.slide-arrow{top:315px;width:22px;height:22px;border-radius:50%;background:rgba(60,60,60,.55)}
.slide-dot{top:514px;width:8px;height:8px;border-radius:50%;border:1px solid #555;background:#fff}

/* content */
.page-bg{left:0;top:534px;width:1029px;height:506px;background:var(--page)}
.content-panel{left:117px;top:534px;width:795px;height:506px;background:linear-gradient(#e2e2de,var(--panel) 60px)}
.welcome-title{left:132px;top:550px;font-family:"Josefin Sans",sans-serif;font-size:28px;color:var(--ink)}
.welcome-copy{left:132px;top:587px;width:516px;font-size:11px;line-height:13px;color:var(--text)}
.welcome-copy p{margin-bottom:14px}

.services-box{left:132px;top:772px;width:532px;height:255px;border:1px solid var(--box-line);border-radius:3px;background:linear-gradient(#f4f4f1,#dfe1dc)}
.section-title{font-family:"Josefin Sans",sans-serif;font-size:21px;color:var(--ink)}
.box-copy{font-size:11px;line-height:15.5px;color:var(--ink)}
.benefit-list{list-style:none;font-size:11px;color:var(--ink)}
.benefit-list li{height:18px;display:flex;align-items:center;gap:3px}

/* sidebar */
.side-box{left:698px;width:198px;border:1px solid #cfcfcb;border-radius:3px;background:#f3f3ef}
.side-head{height:35px;background:linear-gradient(var(--head-top),var(--head-bottom));color:#fff;font-family:"Josefin Sans",sans-serif;font-size:20px;text-align:center;line-height:38px}
.field{left:12px;width:168px;height:20px;background:var(--field);border:1px solid var(--field-line);font-size:10px;color:var(--muted);padding:3px 7px}
.send-button{left:62px;top:251px;width:74px;height:23px;background:linear-gradient(var(--head-top),var(--head-bottom));border:1px solid #222;border-radius:3px;color:#fff;font-size:10px;text-align:center;line-height:21px}
.gallery-image{left:10px;top:50px;width:175px;height:105px;border:1px solid #ccc;background:linear-gradient(90deg,#3a4a3a,#6c8a5a 40%,#b7b7ac 70%,#d8d8d2)}

/* footer */
.site-footer{left:0;top:1040px;width:1029px;height:136px;background:var(--footer)}
.footer-links{left:139px;top:1076px;list-style:none;color:var(--footer-text);font-size:12px;line-height:18px}
.footer-name{left:696px;top:1072px;color:#fff;font-family:"Josefin Sans",sans-serif;font-size:19px}
.footer-address{left:696px;top:1091px;color:#fff;font-size:12px;line-height:13px}
.footer-line{color:#fff;font-size:12px;display:flex;align-items:center;gap:8px}
.footer-bar{left:0;top:1176px;width:1029px;height:24px;background:var(--footer-bar);color:var(--footer-muted);font-size:11px;text-align:center;line-height:24px}
</style>
</head>
<body>

<header class="abs site-header">
  <div class="abs brand-name">Milos Meadow</div>
  <div class="abs brand-tag">indoor plant hire</div>
  <span class="abs social" style="left:804px"></span>
  <span class="abs social" style="left:838px"></span>
  <span class="abs social" style="left:873px"></span>
  <div class="abs header-phone">
    <svg width="22" height="22" viewBox="0 0 24 24"><path d="M6.6 10.8c1.4 2.8 3.8 5.1 6.6 6.6l2.2-2.2c.3-.3.7-.4 1-.2 1.1.4 2.3.6 3.6.6.6 0 1 .4 1 1V20c0 .6-.4 1-1 1C10.6 21 3 13.4 3 4c0-.6.4-1 1-1h3.5c.6 0 1 .4 1 1 0 1.2.2 2.4.6 3.6.1.3 0 .7-.2 1z" fill="#222"/></svg>
    027 555 0184
  </div>
  <div class="abs header-mail">
    <svg width="22" height="16" viewBox="0 0 22 16"><rect x="1" y="2" width="20" height="13" fill="#e8c77a" stroke="#b38a3a"/><path d="M1 2l10 7 10-7" fill="none" stroke="#b38a3a"/></svg>
    info@milosmeadow.com
  </div>
</header>

<nav class="abs main-nav">
  <a href="#" style="left:132px">Home</a>
  <a href="#" style="left:204px">Products</a>
  <a href="#" style="left:301px">Gallery</a>
  <a href="#" style="left:386px">Contact Us</a>
</nav>

<section class="abs slider-band"></section>
<div class="abs slider-frame"></div>
<div class="abs slide-image" role="img" aria-label="Photo of potted indoor plants in tall grey planters beside an armchair and a garden window"></div>
<span class="abs slide-arrow" style="left:134px"></span>
<span class="abs slide-arrow" style="left:874px"></span>
<span class="abs slide-dot" style="left:488px"></span>
<span class="abs slide-dot" style="left:503px"></span>
<span class="abs slide-dot" style="left:518px"></span>
<span class="abs slide-dot" style="left:533px"></span>

<div class="abs page-bg"></div>
<main class="abs content-panel"></main>

<h1 class="abs welcome-title">Welcome to Milo’s Meadow</h1>
<div class="abs welcome-copy">
  <p>Milos Meadow is a family owned, Christchurch based business established over 25 years ago.</p>
  <p>We can enhance your workplace by introducing quality indoor plants in attractive planters. Creating a natural green environment with Milos Meadow plants will help improve indoor air quality, increase staff wellness and productivity.</p>
  <p>Our range of tropical and native plants will enhance your conference or event by creating a more relaxing atmosphere for your delegates or clients. Milos Meadow staff can advise on plant arrangement, deliver and setup for each event.</p>
  <p>We are committed to providing prompt friendly service to all our customers ensuring that your workplace or function is enhanced with quality Milos Meadow plants</p>
</div>

<section class="abs services-box">
  <h2 class="abs section-title" style="left:14px;top:6px">Services</h2>
  <p class="abs box-copy" style="left:13px;top:32px;width:500px">Long term indoor plant hire – Commercial offices, receptions, showrooms, hospitality<br>Short term indoor and outdoor plant hire – Events, conferences, promotions, weddings, trade shows, field days</p>
  <h2 class="abs section-title" style="left:14px;top:97px;font-size:18px">Benefits</h2>
  <p class="abs box-copy" style="left:13px;top:115px">Family Owned Christchurch based businessesPromt, efficient and friendlyfield days</p>
  <ul class="abs benefit-list" style="left:14px;top:138px">
    <li><svg width="12" height="12" viewBox="0 0 12 12"><path d="M6 .5l1.6 3.4 3.7.4-2.8 2.5.8 3.7L6 8.6 2.7 10.5l.8-3.7L.7 4.3l3.7-.4z" fill="var(--star)"/></svg>7 day per week service</li>
    <li><svg width="12" height="12" viewBox="0 0 12 12"><path d="M6 .5l1.6 3.4 3.7.4-2.8 2.5.8 3.7L6 8.6 2.7 10.5l.8-3.7L.7 4.3l3.7-.4z" fill="var(--star)"/></svg>On-site advice and quotes</li>
    <li><svg width="12" height="12" viewBox="0 0 12 12"><path d="M6 .5l1.6 3.4 3.7.4-2.8 2.5.8 3.7L6 8.6 2.7 10.5l.8-3.7L.7 4.3l3.7-.4z" fill="var(--star)"/></svg>Competitive hire charges</li>
    <li><svg width="12" height="12" viewBox="0 0 12 12"><path d="M6 .5l1.6 3.4 3.7.4-2.8 2.5.8 3.7L6 8.6 2.7 10.5l.8-3.7L.7 4.3l3.7-.4z" fill="var(--star)"/></svg>Quality plants and planters</li>
    <li><svg width="12" height="12" viewBox="0 0 12 12"><path d="M6 .5l1.6 3.4 3.7.4-2.8 2.5.8 3.7L6 8.6 2.7 10.5l.8-3.7L.7 4.3l3.7-.4z" fill="var(--star)"/></svg>Regular plant maintenance</li>
    <li><svg width="12" height="12" viewBox="0 0 12 12"><path d="M6 .5l1.6 3.4 3.7.4-2.8 2.5.8 3.7L6 8.6 2.7 10.5l.8-3.7L.7 4.3l3.7-.4z" fill="var(--star)"/></svg>No fixed terms contract necessary</li>
  </ul>
  <ul class="abs benefit-list" style="left:248px;top:138px">
    <li><svg width="12" height="12" viewBox="0 0 12 12"><path d="M6 .5l1.6 3.4 3.7.4-2.8 2.5.8 3.7L6 8.6 2.7 10.5l.8-3.7L.7 4.3l3.7-.4z" fill="var(--star)"/></svg>Enhances the appearance of your workplace</li>
    <li><svg width="12" height="12" viewBox="0 0 12 12"><path d="M6 .5l1.6 3.4 3.7.4-2.8 2.5.8 3.7L6 8.6 2.7 10.5l.8-3.7L.7 4.3l3.7-.4z" fill="var(--star)"/></svg>Provides a natural and tranquil environment</li>
    <li><svg width="12" height="12" viewBox="0 0 12 12"><path d="M6 .5l1.6 3.4 3.7.4-2.8 2.5.8 3.7L6 8.6 2.7 10.5l.8-3.7L.7 4.3l3.7-.4z" fill="var(--star)"/></svg>Provides interior landscaping variety and versatility</li>
    <li><svg width="12" height="12" viewBox="0 0 12 12"><path d="M6 .5l1.6 3.4 3.7.4-2.8 2.5.8 3.7L6 8.6 2.7 10.5l.8-3.7L.7 4.3l3.7-.4z" fill="var(--star)"/></svg>Provids a claming atmosphere for clients and staff</li>
    <li><svg width="12" height="12" viewBox="0 0 12 12"><path d="M6 .5l1.6 3.4 3.7.4-2.8 2.5.8 3.7L6 8.6 2.7 10.5l.8-3.7L.7 4.3l3.7-.4z" fill="var(--star)"/></svg>No staff down time due to gardenin</li>
    <li><svg width="12" height="12" viewBox="0 0 12 12"><path d="M6 .5l1.6 3.4 3.7.4-2.8 2.5.8 3.7L6 8.6 2.7 10.5l.8-3.7L.7 4.3l3.7-.4z" fill="var(--star)"/></svg>Speciment plants up to 2.5m tall available</li>
  </ul>
</section>

<aside class="abs side-box" style="top:556px;height:287px">
  <div class="side-head">Quick Enquiry</div>
  <div class="abs field" style="top:40px">Enter your name</div>
  <div class="abs field" style="top:65px">Enter Company name</div>
  <div class="abs field" style="top:89px">Enter post code</div>
  <div class="abs field" style="top:113px">Enter tel no.</div>
  <div class="abs field" style="top:137px">Enter email id</div>
  <div class="abs field" style="top:161px;height:81px;padding-top:6px">Enter message</div>
  <div class="abs send-button">Send Enquiry</div>
</aside>

<aside class="abs side-box" style="top:856px;height:171px">
  <div class="side-head">Gallery</div>
  <div class="abs gallery-image" role="img" aria-label="Photo of a row of upright snake plants in a white planter"></div>
</aside>

<footer class="abs site-footer"></footer>
<ul class="abs footer-links">
  <li>Home</li><li>Products</li><li>Gallery</li><li>Contact Us</li>
</ul>
<svg class="abs" style="left:679px;top:1074px" width="12" height="17" viewBox="0 0 12 17"><path d="M6 1a5 5 0 0 0-5 5c0 4 5 10 5 10s5-6 5-10a5 5 0 0 0-5-5z" fill="none" stroke="#bbb" stroke-width="1.5"/><circle cx="6" cy="6" r="1.8" fill="#bbb"/></svg>
<div class="abs footer-name">Milos Meadow</div>
<div class="abs footer-address">58 Harlow Lane, Fernside,<br>Christchurch City, Canterbury</div>
<div class="abs footer-line" style="left:677px;top:1129px">
  <svg width="11" height="15" viewBox="0 0 11 15"><rect x="1" y="1" width="9" height="13" rx="1.5" fill="none" stroke="#bbb" stroke-width="1.5"/><rect x="4" y="11" width="3" height="1.5" fill="#bbb"/></svg>027 555 0184
</div>
<div class="abs footer-line" style="left:677px;top:1153px">
  <svg width="12" height="12" viewBox="0 0 12 12"><path d="M1 5l5-4 5 4v6H1z" fill="none" stroke="#bbb" stroke-width="1.3"/><path d="M1 5l5 3 5-3" fill="none" stroke="#bbb" stroke-width="1.3"/></svg>info@milosmeadow.com
</div>
<div class="abs footer-bar">Copyright © 2013 Milos Meadow. All rights reserved</div>

</body>
</html>
```